Tag design needed for wall art products

We need to design a tag for wall art products, which are Canvas, wood art, and rolling canvas.

The Tag need to be classical which means not too colorful, all information in the file (1pic) need to be included such as brand name, company website.

The side of tag need to be same as Kavrix 6 or Kavrix 7 with a hole on the top.
Updates

More designs are required!

Target Market(s)

US Market

Industry/Entity Type

Home And Garden

Requirements
Must have
• ART.DECORATION
• BRENDITH&TULIVARE
• 1978
• WWW.TULIVAREHUE.EXAMPLE
• HONGKONG AUSTRALIA CHINA

```html
<!DOCTYPE html>
<html lang="en">
<head>
<meta charset="utf-8">
<title>Brendith &amp; Tulivare – Hang Tags</title>
<link rel="stylesheet" href="https://fonts.googleapis.com/css2?family=Open+Sans:wght@400;700&display=swap">
<style>
  :root {
    --page: #ffffff;
    --string: #8a5a34;
    --kraft: #ddd3c4;
    --kraft-light: #e8e0d4;
    --brown: #7a4e2c;
    --brown-soft: #9a7152;
    --chevron-dark: #c9c9c9;
    --chevron-light: #efefef;
    --grey: #8c8c8c;
    --ink: #111111;
    --panel: #ffffff;
  }
  * { box-sizing: border-box; margin: 0; padding: 0; }
  html, body { width: 1042px; height: 1200px; overflow: hidden; background: var(--page); }
  .stage {
    position: absolute; left: 0; top: 0;
    width: 640px; height: 737px;
    transform: scale(1.628); transform-origin: 0 0;
  }
  .strings { position: absolute; left: 0; top: 0; width: 640px; height: 737px; z-index: 3; pointer-events: none; }
  .tag {
    position: absolute; top: 210px; width: 240px; height: 487px;
    border-radius: 22px; overflow: hidden;
  }
  .tag--kraft { left: 67px; }
  .tag--chevron { left: 336px; }
  .tag__surface { position: absolute; inset: 0; }
  .tag--kraft .tag__surface {
    background: radial-gradient(ellipse at 40% 60%, var(--kraft-light), var(--kraft) 70%);
  }
  .tag--chevron .tag__surface {
    background: linear-gradient(160deg, var(--chevron-light), var(--chevron-dark) 50%, var(--chevron-light));
  }
  .tag__hole {
    position: absolute; top: 7px; left: 50%; width: 23px; height: 23px;
    margin-left: -11.5px; border-radius: 50%; background: var(--page);
  }
  .label { position: absolute; left: 13px; top: 90px; width: 214px; height: 218px; }
  .tag--chevron .label { left: 14px; top: 95px; }
  .label__ornament { position: absolute; left: 0; width: 100%; height: 44px; border-radius: 6px; }
  .label__ornament--top { top: 0; }
  .label__ornament--bottom { bottom: 0; }
  .tag--kraft .label__ornament { background: linear-gradient(var(--panel), #efe4d9); border: 1px solid var(--brown-soft); }
  .tag--chevron .label__ornament { background: linear-gradient(var(--panel), #e6e6e6); border: 1px solid var(--grey); }
  .label__panel {
    position: absolute; left: 8px; right: 8px; top: 36px; bottom: 36px;
    background: var(--panel); border: 2px solid var(--brown);
    display: flex; align-items: center; justify-content: center;
    text-align: center;
  }
  .tag--chevron .label__panel { border-color: var(--grey); border-radius: 10px; }
  .label__name {
    font-family: "Open Sans", sans-serif; font-weight: 700; font-size: 15px;
    color: var(--ink); letter-spacing: 0.2px; white-space: nowrap;
  }
  .tag__line {
    position: absolute; left: 0; right: 0; text-align: center;
    font-family: "Open Sans", sans-serif; white-space: nowrap;
  }
  .tag__category { top: 336px; font-size: 11.5px; font-weight: 400; color: var(--brown); }
  .tag__web { top: 381px; font-size: 13px; font-weight: 700; color: var(--brown); }
  .tag__regions { top: 421px; font-size: 11.5px; font-weight: 400; color: var(--brown); }
  .tag--chevron .tag__category,
  .tag--chevron .tag__web,
  .tag--chevron .tag__regions { color: var(--ink); }
</style>
</head>
<body>
<div class="stage">
  <svg class="strings" viewBox="0 0 640 737" aria-hidden="true">
    <g fill="none" stroke="#8a5a34" stroke-width="2">
      <path d="M128 12 C150 70 200 120 188 170 C180 200 176 212 182 226"/>
      <path d="M196 70 C192 120 160 160 176 200 C182 212 190 216 186 226"/>
      <path d="M180 230 C176 216 194 216 190 230"/>
      <path d="M400 12 C420 70 470 120 458 170 C450 200 446 212 452 226"/>
      <path d="M466 70 C462 120 430 160 446 200 C452 212 460 216 456 226"/>
      <path d="M450 230 C446 216 464 216 460 230"/>
    </g>
  </svg>

  <article class="tag tag--kraft">
    <div class="tag__surface" role="img" aria-label="Beige kraft paper texture with faint white speckles"></div>
    <div class="tag__hole"></div>
    <div class="label">
      <div class="label__ornament label__ornament--top" role="img" aria-label="Brown scrollwork flourish crowning the label"></div>
      <div class="label__ornament label__ornament--bottom" role="img" aria-label="Brown scrollwork flourish beneath the label"></div>
      <div class="label__panel">
        <p class="label__name">BRENDITH&amp;TULIVARE</p>
      </div>
    </div>
    <p class="tag__line tag__category">ART.DECORATION • 1978</p>
    <p class="tag__line tag__web">WWW.TULIVAREHUE.EXAMPLE</p>
    <p class="tag__line tag__regions">HONGKONG • AUSTRALIA • CHINA</p>
  </article>

  <article class="tag tag--chevron">
    <div class="tag__surface" role="img" aria-label="Grey and white zigzag chevron pattern"></div>
    <div class="tag__hole"></div>
    <div class="label">
      <div class="label__ornament label__ornament--top" role="img" aria-label="Grey scrollwork flourish crowning the label"></div>
      <div class="label__ornament label__ornament--bottom" role="img" aria-label="Grey scrollwork flourish beneath the label"></div>
      <div class="label__panel">
        <p class="label__name">BRENDITH&amp;TULIVARE</p>
      </div>
    </div>
    <p class="tag__line tag__category">ART.DECORATION • 1978</p>
    <p class="tag__line tag__web">WWW.TULIVAREHUE.EXAMPLE</p>
    <p class="tag__line tag__regions">HONGKONG • AUSTRALIA • CHINA</p>
  </article>
</div>
</body>
</html>
```